Flyer-Design für Betreuung von pflegebedürftigen/hilfebedürftigen Senioren
Ich bin begeistert! Sehr gute und geduldige Bearbeitung meiner Änderungswünsche. Gute und schnelle Kommunikation. Danke!
Zielgruppe
Alltagshilfe, Betreuung, Begleitung und Unterstützung von pflegebedürftigen/hilfebedürftigen Senioren
Wir begleiten Senioren im Alltag, in Ihrer Freizeit, zu Ausflügen und Veranstaltungen, oder einfach mal zum Kaffee trinken. Wir erledigen Einkäufe, unterstützen bei Arzt und Behördengängen oder haben einfach nur ein offenes Ohr und schenken unsere Zeit. Gesellschaftsspiele, Gedächtnistraining und Erinnerungspflege für die kognitive Aktivierung kommen unter anderem bei den betreuen Demenzkranken zum Einsatz. Auch die physische Aktivierung in Form von Spaziergängen oder Bewegungsübungen gehört zum Arbeitsalltag.
Wir betreuuen die Senioren stundenweise im eigenen häuslichen Umfeld. Dadurch werden deren pflegende Angehörige entlastet und der Senior dabei unterstützt, seine Eigenständigkeit zu erhalten.
Aufgabenstellung
Nach Möglichkeit hätte ich gern Bilder eingebunden, auf denen keine Menschen sondern eher Figuren zu sehen sind, welche Liebe, Zusammenhalt, Familie und Unterstützung suggerieren, ähnlich wie bei dem Beispielflyer den ich mit hochlade. Die Schrift sollte Seniorengerecht und evtl. in Anlehnung an das Logo sein (Lindauer Altenbeistand - Helvetica Neue - 43 Light Extended / Slogan - Lato - Bold ). Die Farben des Logos, welche sich gern im Flyer wiederfinden dürfen sind: Rot: #BA2428 ; Orange: #F26C21
Vielleicht könnte man Puzzleteile kreativ einarbeiten? Senioren- und Alltagsbegleitung im häuslichen Umfeld ist ja einer von mehreren Bausteinen (neben Pflegedienst ect) der die Angehörigen entlastet und die Senioren unterstützt um den Alltag solange wie möglich in den eigenen 4 Wänden zu organisieren.. Allerdings kein Muss, nur ein Gedanke.
Auch bezüglich des Textes bin ich noch nicht 100% sicher. Gibt es die Möglichkeit, ein Vorgesehenes Textfeld nach dem Erwerb des Designs selbst zu ändern? Am besten mit Microsoft Word, oder so?

```html
<!DOCTYPE html>
<html lang="de">
<head>
<meta charset="utf-8">
<title>Lindauer Altenbeistand – Flyer</title>
<link href="https://fonts.googleapis.com/css2?family=Lato:wght@300;400;700;900&display=swap" rel="stylesheet">
<style>
  :root{
    --stage:#e2e3e5;
    --paper:#f5f5f4;
    --red:#ba2428;
    --red-deep:#a3161f;
    --orange:#f26c21;
    --orange-warm:#e05a0c;
    --ink:#3a3a3a;
    --note:#5a5a5a;
    --white:#ffffff;
  }
  *{margin:0;padding:0;box-sizing:border-box}
  html,body{width:1200px;height:2400px;overflow:hidden}
  body{background:var(--stage);font-family:"Lato",Arial,sans-serif;position:relative}

  .flyer-page{position:absolute;width:490px;height:1047px;background:var(--paper);overflow:hidden}
  .flyer-page--front{left:361px;top:91px}
  .flyer-page--back{left:370px;top:1228px}
  .page-shapes{position:absolute;inset:0;width:490px;height:1047px}

  /* brand block */
  .brand{position:absolute;left:0;top:70px;width:490px}
  .brand__dot{position:absolute;left:42px;top:22px;width:64px;height:64px;border-radius:50%;background:var(--orange)}
  .brand__name{position:absolute;left:138px;top:0;font-weight:300;font-size:36px;line-height:37px;color:var(--red)}
  .brand__owner{position:absolute;left:138px;top:82px;font-weight:700;font-size:22px;line-height:26px;color:var(--orange)}
  .brand__tagline{position:absolute;left:0;width:490px;top:120px;text-align:center;font-weight:400;font-size:15px;line-height:18px;color:var(--red)}

  /* front */
  .service-hub{position:absolute;left:0;top:0}
  .hub-photo{position:absolute;left:121px;top:390px;width:248px;height:248px;border-radius:50%;
    background:radial-gradient(circle at 65% 45%,#e9c2a8 0 22%,#c99b82 30%,#9aa37a 55%,#6f8a4c 80%)}
  .hub-icon{position:absolute;width:44px;height:44px;border-radius:50%;background:var(--orange);opacity:.9}

  .front-headline{position:absolute;left:0;top:850px;width:490px;text-align:center;color:var(--white);
    font-weight:700;font-size:41px;line-height:46px}
  .front-url{position:absolute;left:0;top:995px;width:490px;text-align:center;color:var(--white);font-weight:700;font-size:18px}

  /* back */
  .services-title{position:absolute;left:33px;top:52px;color:var(--red);font-weight:900;font-size:54px;line-height:62px}
  .services-list{position:absolute;left:33px;top:206px;list-style:none;width:440px}
  .services-list li{position:relative;padding-left:39px;font-size:20.5px;line-height:25px;color:var(--ink);margin-bottom:16px}
  .services-list .tick{position:absolute;left:0;top:0;width:22px;height:24px}
  .funding-note{position:absolute;left:33px;top:698px;font-size:13px;line-height:17px;font-weight:700;color:var(--note)}

  .back-footer{position:absolute;left:0;top:760px;width:490px;height:287px;
    background:linear-gradient(100deg,var(--red-deep) 0%,#c22a1e 45%,var(--orange-warm) 75%,var(--red-deep) 100%)}
  .back-footer .brand{top:24px}
  .back-footer .brand__dot{background:var(--white);top:20px;left:36px}
  .back-footer .brand__name,.back-footer .brand__owner,.back-footer .brand__tagline{color:var(--white)}
  .back-footer .brand__tagline{top:118px}
  .contact{position:absolute;left:0;top:170px;width:490px;text-align:center;color:var(--white);font-weight:700;font-size:18px;line-height:23.5px;font-style:normal}
</style>
</head>
<body>

<section class="flyer-page flyer-page--front">
  <svg class="page-shapes" viewBox="0 0 490 1047" aria-hidden="true">
    <defs>
      <linearGradient id="bandFront" x1="0" y1="0" x2="1" y2="0">
        <stop offset="0" stop-color="#a3161f"/><stop offset=".5" stop-color="#e05a0c"/><stop offset="1" stop-color="#a3161f"/>
      </linearGradient>
      <linearGradient id="baseFront" x1="0" y1="0" x2="1" y2="0">
        <stop offset="0" stop-color="#a3161f"/><stop offset=".55" stop-color="#e05a0c"/><stop offset="1" stop-color="#a3161f"/>
      </linearGradient>
    </defs>
    <path d="M0 0H490V30C300 26 110 30 0 67Z" fill="url(#bandFront)"/>
    <path d="M0 822C250 820 430 790 490 696V1047H0Z" fill="url(#baseFront)"/>
    <g stroke="#f26c21" stroke-width="1.5" fill="none" stroke-dasharray="2 3">
      <line x1="245" y1="381" x2="245" y2="350"/>
      <line x1="339" y1="420" x2="364" y2="395"/>
      <line x1="378" y1="514" x2="418" y2="514"/>
      <line x1="339" y1="608" x2="366" y2="634"/>
      <line x1="245" y1="647" x2="245" y2="682"/>
      <line x1="151" y1="608" x2="124" y2="634"/>
      <line x1="112" y1="514" x2="76" y2="514"/>
      <line x1="151" y1="420" x2="130" y2="398"/>
    </g>
    <circle cx="245" cy="514" r="133" fill="none" stroke="#f26c21" stroke-width="2"/>
  </svg>

  <header class="brand">
    <span class="brand__dot"></span>
    <div class="brand__name">Lindauer<br>Altenbeistand</div>
    <div class="brand__owner">Inh. Hanna Folmerit</div>
    <div class="brand__tagline">Zuwendung · Nähe · Verlässlichkeit</div>
  </header>

  <div class="service-hub">
    <div class="hub-photo" role="img" aria-label="Foto: eine ältere Hand ruht in einer jüngeren Hand, grüner Hintergrund"></div>
    <div class="hub-icon" style="left:223px;top:296px" role="img" aria-label="Symbol Schaukelstuhl"></div>
    <div class="hub-icon" style="left:352px;top:347px" role="img" aria-label="Symbol Wollknäuel"></div>
    <div class="hub-icon" style="left:422px;top:492px" role="img" aria-label="Symbol Brille"></div>
    <div class="hub-icon" style="left:366px;top:629px" role="img" aria-label="Symbol Telefon"></div>
    <div class="hub-icon" style="left:223px;top:686px" role="img" aria-label="Symbol Baum"></div>
    <div class="hub-icon" style="left:81px;top:629px" role="img" aria-label="Symbol Gebäude"></div>
    <div class="hub-icon" style="left:27px;top:495px" role="img" aria-label="Symbol Seniorenpaar"></div>
    <div class="hub-icon" style="left:88px;top:346px" role="img" aria-label="Symbol Rollstuhl"></div>
  </div>

  <h1 class="front-headline">Dienstleistungen<br>für Senioren und den<br>Alltag in Dresden</h1>
  <div class="front-url">www.lindauer-altenbeistand.de</div>
</section>

<section class="flyer-page flyer-page--back">
  <svg class="page-shapes" viewBox="0 0 490 1047" aria-hidden="true">
    <defs>
      <linearGradient id="bandBack" x1="0" y1="0" x2="1" y2="0">
        <stop offset="0" stop-color="#a3161f"/><stop offset=".45" stop-color="#e05a0c"/><stop offset="1" stop-color="#a3161f"/>
      </linearGradient>
    </defs>
    <path d="M0 0H490V88C440 40 300 30 0 32Z" fill="url(#bandBack)"/>
  </svg>

  <h2 class="services-title">Unsere<br>Leistungen</h2>

  <ul class="services-list">
    <li><svg class="tick" viewBox="0 0 22 24"><path d="M2 13L8 21L20 2" fill="none" stroke="#ba2428" stroke-width="3.5" stroke-linecap="round" stroke-linejoin="round"/></svg>Unterstützung bei der Alltagsgestaltung</li>
    <li><svg class="tick" viewBox="0 0 22 24"><path d="M2 13L8 21L20 2" fill="none" stroke="#ba2428" stroke-width="3.5" stroke-linecap="round" stroke-linejoin="round"/></svg>Begleitung zum Einkauf und<br>zu Ärzten/Behörden</li>
    <li><svg class="tick" viewBox="0 0 22 24"><path d="M2 13L8 21L20 2" fill="none" stroke="#ba2428" stroke-width="3.5" stroke-linecap="round" stroke-linejoin="round"/></svg>Beratung bei allgemeinen Fragen</li>
    <li><svg class="tick" viewBox="0 0 22 24"><path d="M2 13L8 21L20 2" fill="none" stroke="#ba2428" stroke-width="3.5" stroke-linecap="round" stroke-linejoin="round"/></svg>Besuch von Veranstaltungen,<br>Museen, Theater</li>
    <li><svg class="tick" viewBox="0 0 22 24"><path d="M2 13L8 21L20 2" fill="none" stroke="#ba2428" stroke-width="3.5" stroke-linecap="round" stroke-linejoin="round"/></svg>Ausflüge (z.B. Zoobesuch)</li>
    <li><svg class="tick" viewBox="0 0 22 24"><path d="M2 13L8 21L20 2" fill="none" stroke="#ba2428" stroke-width="3.5" stroke-linecap="round" stroke-linejoin="round"/></svg>Entlastung von pflegenden Angehörigen</li>
    <li><svg class="tick" viewBox="0 0 22 24"><path d="M2 13L8 21L20 2" fill="none" stroke="#ba2428" stroke-width="3.5" stroke-linecap="round" stroke-linejoin="round"/></svg>Körperliche Aktivierung, z.B. Spaziergänge</li>
    <li><svg class="tick" viewBox="0 0 22 24"><path d="M2 13L8 21L20 2" fill="none" stroke="#ba2428" stroke-width="3.5" stroke-linecap="round" stroke-linejoin="round"/></svg>Gespräche über aktuelle Themen<br>und Vergangenes</li>
    <li><svg class="tick" viewBox="0 0 22 24"><path d="M2 13L8 21L20 2" fill="none" stroke="#ba2428" stroke-width="3.5" stroke-linecap="round" stroke-linejoin="round"/></svg>Erinnerungspflege/Biographiearbeit</li>
    <li><svg class="tick" viewBox="0 0 22 24"><path d="M2 13L8 21L20 2" fill="none" stroke="#ba2428" stroke-width="3.5" stroke-linecap="round" stroke-linejoin="round"/></svg>Gesellschaft leisten und Zeit schenken</li>
  </ul>

  <p class="funding-note">Die Kostenübernahme ist bei bestehendem Pflegegrad<br>durch die Pflegekasse möglich.</p>

  <footer class="back-footer">
    <div class="brand">
      <span class="brand__dot"></span>
      <div class="brand__name">Lindauer<br>Altenbeistand</div>
      <div class="brand__owner">Inh. Hanna Folmerit</div>
      <div class="brand__tagline">Zuwendung · Nähe · Verlässlichkeit</div>
    </div>
    <address class="contact">
      Am Lindenhang 12 · 01217 Dresden<br>
      Tel.: 0170 555 18 42<br>
      www.lindauer-altenbeistand.de<br>
      info@lindauer-altenbeistand.de
    </address>
  </footer>
</section>

</body>
</html>
```